KMV letterhead

We need the Letterhead and a page 2 which will be a simpler page - less header space for the design. Use the design you just created for the Business card. Be sure Page 2 allows for a full page of content.

Industry/Entity Type

Business

```html
<!DOCTYPE html>
<html lang="en">
<head>
<meta charset="utf-8">
<title>KMV Tech Group Letterhead</title>
<link rel="stylesheet" href="https://fonts.googleapis.com/css2?family=Lato:wght@400;700;900&display=swap">
<style>
  :root {
    --backdrop: #878887;
    --paper: #ffffff;
    --brand-red: #c8283a;
    --ink-black: #0c0c0c;
    --ink-dark: #1e1e1e;
    --mark-faint: #ebebeb;
    --text-light: #ffffff;
  }
  * { box-sizing: border-box; margin: 0; padding: 0; }
  html, body { width: 1200px; height: 833px; overflow: hidden; }
  body {
    background: var(--backdrop);
    font-family: "Lato", Arial, sans-serif;
    position: relative;
  }
  .sheet {
    position: absolute;
    top: 50px;
    width: 560px;
    height: 725px;
    background: var(--paper);
    overflow: hidden;
  }
  .sheet--first { left: 26px; }
  .sheet--continuation { left: 619px; }

  .header-wave { position: absolute; left: 0; top: 0; display: block; }
  .tagline {
    position: absolute;
    right: 28px;
    top: 12px;
    color: var(--text-light);
    font-size: 8.5px;
    letter-spacing: 0.2px;
  }

  .brand-name {
    position: absolute;
    left: 44px;
    top: 44px;
    color: var(--ink-dark);
    font-weight: 900;
    text-align: center;
    line-height: 1;
  }
  .brand-name .brand-main { display: block; font-size: 38px; letter-spacing: 1px; }
  .brand-name .brand-sub { display: block; font-size: 9px; letter-spacing: 0.4px; margin-top: 2px; }

  .signatory {
    position: absolute;
    right: 132px;
    top: 78px;
    text-align: right;
    line-height: 1;
  }
  .signatory-name { font-size: 14px; color: var(--ink-dark); }
  .signatory-name strong { font-weight: 700; }
  .signatory-title {
    font-size: 7.5px;
    font-weight: 700;
    color: var(--brand-red);
    letter-spacing: 1px;
    margin-top: 2px;
  }

  .contact-list {
    position: absolute;
    left: 452px;
    top: 60px;
    list-style: none;
    font-size: 5.6px;
    line-height: 9px;
    color: var(--ink-dark);
  }
  .contact-list li { display: flex; align-items: center; gap: 3px; }
  .contact-list svg { width: 6px; height: 6px; fill: var(--brand-red); }

  .watermark {
    position: absolute;
    left: 308px;
    top: 584px;
    color: var(--mark-faint);
    font-weight: 900;
    text-align: center;
    line-height: 1;
  }
  .watermark .brand-main { display: block; font-size: 72px; letter-spacing: 4px; }
  .watermark .brand-sub { display: block; font-size: 16px; letter-spacing: 0.5px; }

  .footer-band {
    position: absolute;
    left: 0;
    bottom: 0;
    width: 100%;
    height: 31px;
    background: var(--brand-red);
    color: var(--text-light);
    font-size: 8px;
    display: flex;
    align-items: center;
    justify-content: center;
    gap: 4px;
  }
  .footer-band svg { width: 9px; height: 7px; stroke: var(--text-light); fill: none; stroke-width: 0.8; }
</style>
</head>
<body>

<section class="sheet sheet--first" aria-label="Letterhead page one">
  <svg class="header-wave" width="560" height="48" viewBox="0 0 560 48">
    <path fill="var(--brand-red)" d="M0,10 C160,2 360,22 560,30 L560,38 C360,30 170,28 0,45 Z"/>
    <path fill="var(--ink-black)" d="M0,0 H560 V34 C360,26 160,2 0,14 Z"/>
  </svg>
  <p class="tagline">Woman Owned Small Business</p>

  <div class="brand-name">
    <span class="brand-main">KMV</span>
    <span class="brand-sub">TECH GROUP</span>
  </div>

  <div class="signatory">
    <p class="signatory-name">Dana <strong>Marsh</strong></p>
    <p class="signatory-title">PRESIDENT</p>
  </div>

  <ul class="contact-list">
    <li><svg viewBox="0 0 10 10"><path d="M2 0h2l1 3-1.5 1a6 6 0 0 0 2.5 2.5L7 5l3 1v2a2 2 0 0 1-2 2C4 10 0 6 0 2a2 2 0 0 1 2-2z"/></svg>: 240.555.0132</li>
    <li><svg viewBox="0 0 10 10"><path d="M5 0l5 5H8v5H2V5H0z"/></svg>: 240.555.0178</li>
    <li><svg viewBox="0 0 10 10"><rect x="2.5" y="0" width="5" height="10" rx="1"/></svg>: 703.555.0194</li>
    <li><svg viewBox="0 0 10 10"><path d="M0 2h10v6H0z M0 2l5 4 5-4" /></svg>: dana@kmvtechgroup.com</li>
    <li><svg viewBox="0 0 10 10"><circle cx="5" cy="5" r="5"/></svg>: www.kmvtechgroup.com</li>
  </ul>

  <div class="watermark" aria-hidden="true">
    <span class="brand-main">KMV</span>
    <span class="brand-sub">TECH GROUP</span>
  </div>

  <footer class="footer-band">
    <svg viewBox="0 0 9 7"><rect x="0.5" y="0.5" width="8" height="6"/><path d="M0.5 0.5l4 3.5 4-3.5"/></svg>
    <span>2250 Harbor Lane, Suite 310, Fairview, MD20877</span>
  </footer>
</section>

<section class="sheet sheet--continuation" aria-label="Letterhead page two">
  <svg class="header-wave" width="560" height="30" viewBox="0 0 560 30">
    <path fill="var(--brand-red)" d="M0,8 C160,2 360,12 560,20 L560,26 C360,20 170,14 0,30 Z"/>
    <path fill="var(--ink-black)" d="M0,0 H560 V24 C360,16 160,0 0,12 Z"/>
  </svg>

  <div class="watermark" aria-hidden="true">
    <span class="brand-main">KMV</span>
    <span class="brand-sub">TECH GROUP</span>
  </div>

  <footer class="footer-band">
    <span>2250 Harbor Lane, Suite 310, Fairview, MD20877</span>
  </footer>
</section>

</body>
</html>
```